Doctor in Veterinary Medecine/ veterinarian

I am a vet and would like a buisness card which is simple yet elegant and professional.
My aim is to help as much animals as I can. My main field of expertise are dogs and cats. I would like the card to reflect a "family doctor" feeling.
It should not be the traditional picture of a paw or a dog but yet it should have a sign of a pet on it. I would like to have my name Lina Haddoul as well as my profession D.V.M and my number.

Target Market(s)

Lebanese population who have pets

Industry/Entity Type

Doctor

Contact Information for Business Card

Should contain my profession " D.V.M", my full name "Lina Haddoul" and my number "0096171539214"

Requirements
Must have
• A certain picture depicting my profession
Nice to have
• Some sort of picture related to pets and animals
Should not have
• A picture of a paw or a dog. I need something more creative

```html
<!DOCTYPE html>
<html lang="en">
<head>
<meta charset="utf-8">
<title>Dr. Lina Haddoul – Business Card</title>
<link href="https://fonts.googleapis.com/css2?family=Questrial&family=Arimo:wght@400;700&display=swap" rel="stylesheet">
<style>
  :root {
    --backdrop: #ece8e3;
    --card: #ffffff;
    --brand-blue: #29a8e0;
    --brand-green: #7bc043;
    --text-grey: #b5b5b5;
    --muted-grey: #a9a9a9;
  }
  html, body {
    margin: 0;
    padding: 0;
    width: 1200px;
    height: 1000px;
    overflow: hidden;
    background: var(--backdrop);
  }
  .canvas {
    position: relative;
    width: 1200px;
    height: 1000px;
  }
  .business-card {
    position: absolute;
    left: 100px;
    top: 202px;
    width: 1000px;
    height: 596px;
    background: var(--card);
    border-radius: 36px;
    box-shadow: 0 6px 18px rgba(0,0,0,0.12);
    text-align: center;
  }
  .brand-mark {
    position: absolute;
    left: 50%;
    top: 100px;
    width: 130px;
    height: 130px;
    margin-left: -65px;
    border-radius: 50%;
    background: var(--brand-green);
  }
  .brand-name {
    position: absolute;
    left: 0;
    right: 0;
    top: 285px;
    margin: 0;
    font-family: "Questrial", "Century Gothic", sans-serif;
    font-weight: 400;
    font-size: 56px;
    letter-spacing: 0.5px;
    line-height: 1;
    color: var(--brand-blue);
  }
  .brand-tagline {
    position: absolute;
    left: 0;
    right: 0;
    top: 352px;
    margin: 0;
    font-family: "Questrial", "Century Gothic", sans-serif;
    font-size: 40px;
    line-height: 1;
    color: var(--text-grey);
  }
  .doctor-name {
    position: absolute;
    left: 0;
    right: 0;
    top: 470px;
    margin: 0;
    font-family: "Arimo", Arial, sans-serif;
    font-size: 29px;
    line-height: 1;
    color: var(--muted-grey);
  }
  .doctor-name strong { font-weight: 700; }
  .phone {
    position: absolute;
    left: 0;
    right: 0;
    top: 526px;
    margin: 0;
    font-family: "Arimo", Arial, sans-serif;
    font-size: 25px;
    line-height: 1;
    color: var(--muted-grey);
    display: flex;
    justify-content: center;
    align-items: center;
    gap: 10px;
  }
  .phone svg { width: 26px; height: 20px; fill: var(--muted-grey); }
</style>
</head>
<body>
  <main class="canvas">
    <section class="business-card">
      <div class="brand-mark" aria-hidden="true"></div>
      <h1 class="brand-name">DR.LINAHADDOUL</h1>
      <p class="brand-tagline">Veterinary</p>
      <p class="doctor-name"><strong>Dr.Lina Haddoul</strong>, D.V.M</p>
      <p class="phone">
        <svg viewBox="0 0 26 20" aria-hidden="true">
          <path d="M2 6 C2 2 24 2 24 6 L24 8 L18 8 L18 5.5 C15 4.5 11 4.5 8 5.5 L8 8 L2 8 Z"/>
          <path d="M6 9 L20 9 L23 18 L3 18 Z"/>
          <circle cx="13" cy="13.5" r="2.6" fill="#ffffff"/>
        </svg>
        <span>0096171539214</span>
      </p>
    </section>
  </main>
</body>
</html>
```